KO-LNE , Artificial hedge flyer

i need new flyer, in att i'm sending old one but as we produce artificial flowers, trees and most popular is artificial green hedge, and it's used from variety places, from swimming pool, restaurants, bars, private terrace, gardens, to protect from neighbor :-) . from beginning is all our product, it's not imported from other producer. we are doing it by measure what we get from customer ( tailor made ) , we give guaranty 15-20 years on all weather that will not loos color, etc.. you can see some pictures in att on old flyer, and some new pictures of same in space newly added. we'd like more pictures with samples of use, etc.you can see our product on www.ko-lne.hr so you can closely known what we are producing, and what for we need new flyer. we have plenty of new picture that are not on our web, so i can use it for new flyer.

Font styles to use
Sans Serif

Requirements
Must have
• company logo, contact info ( sent in word document in att ), logo of croatian product ( on old flyer in att on front side), stamp Quality since 1950 if you could change year to 1960, last time they made mistake and write 1950 ),
Nice to have
• flyer 3 fold type, or if you think it will look better only double side flyer, depend of design and theme so everyone can understand what is our business

```html
<!DOCTYPE html>
<html lang="hr">
<head>
<meta charset="utf-8">
<title>KO-LNE d.o.o. – umjetna živica, letak</title>
<link rel="stylesheet" href="https://fonts.googleapis.com/css2?family=Lobster&family=Montserrat:wght@400;500;600;700;800&display=swap">
<style>
  :root{
    --green:#3bb44a;
    --green-dark:#1f8a3a;
    --lime:#8dc63f;
    --lime-deep:#6cbf3a;
    --teal:#1aa5b5;
    --teal-ink:#16706a;
    --panel-gray:#d2d2d2;
    --ink:#1b1b1b;
    --wood:#eeede9;
    --page:#efefef;
    --white:#ffffff;
    --logo-gray:#6e7475;
  }
  *{box-sizing:border-box;margin:0;padding:0}
  html,body{width:1069px;height:1200px;overflow:hidden;background:var(--page)}
  body{font-family:"Montserrat",Arial,sans-serif;color:var(--ink);position:relative}
  .sheet{position:absolute;left:154px;width:760px;height:570px;background:var(--white);overflow:hidden;box-shadow:0 2px 10px rgba(0,0,0,.12)}
  .sheet--front{top:20px}
  .sheet--back{top:610px}
  .sheet svg.art{position:absolute;inset:0;width:760px;height:570px}
  .abs{position:absolute}
  .wordmark{display:flex;align-items:center;gap:7px;font-family:"Montserrat",sans-serif;font-weight:700;font-size:24px;letter-spacing:.5px;white-space:nowrap}
  .wordmark__dot{width:14px;height:14px;border-radius:50%;display:inline-block}
  .wordmark--light{color:var(--white)}
  .wordmark--light .wordmark__dot{background:var(--white)}
  .wordmark--gray{color:var(--logo-gray)}
  .wordmark--gray .wordmark__dot{background:var(--green)}
  .script{font-family:"Lobster",cursive}
  .quality{left:248px;top:133px;width:104px;height:104px;display:flex;flex-direction:column;align-items:center;justify-content:center;color:var(--white);text-align:center;line-height:1}
  .quality__star{font-size:14px}
  .quality__word{font-weight:800;font-size:19px;letter-spacing:.5px;margin:3px 0}
  .quality__year{font-family:"Lobster",cursive;font-size:16px}
  .quality__stars{font-size:11px;margin-top:3px;letter-spacing:2px}
  .salon-title{left:355px;top:192px;width:145px;color:var(--teal-ink);font-size:19px;line-height:1.05}
  .contact-list{list-style:none;font-size:10px;line-height:1.45;color:#2a2a2a}
  .contact-list li{display:flex;align-items:center;gap:5px}
  .contact-list svg{width:9px;height:9px;flex:none}
  .salon-contacts{left:258px;top:264px}
  .seat-title{left:258px;top:318px;color:var(--teal-ink);font-size:17px}
  .seat-contacts{left:258px;top:342px}
  .web{left:355px;top:533px;display:flex;align-items:center;gap:5px;font-weight:700;font-size:13px;color:var(--green-dark)}
  .web svg{width:12px;height:12px}
  .tagline{left:505px;top:58px;width:250px;text-align:center;color:var(--teal);font-size:22px;line-height:1.05}
  .badge-round{display:flex;align-items:center;justify-content:center;text-align:center;color:var(--white)}
  .inout-badge{left:503px;top:436px;width:84px;height:84px;font-family:"Lobster",cursive;font-size:14px;line-height:1.05}
  .service-title{left:594px;top:484px;font-weight:600;font-size:21px;letter-spacing:1.5px;color:var(--green)}
  .service-text{left:592px;top:512px;width:160px;font-size:8.5px;line-height:1.2;color:var(--teal-ink)}
  .history{left:18px;top:78px;width:250px;font-size:11.5px;font-weight:500;line-height:1.25}
  .offer{left:315px;top:12px;width:420px;text-align:center;color:var(--white);font-size:11.5px;font-weight:500;line-height:1.3}
  .warranty{left:467px;top:147px;width:76px;height:76px;font-size:8.5px;font-weight:700;line-height:1.15}
  .clients{left:218px;top:510px;width:240px;text-align:center;color:var(--white);font-size:11px;font-weight:500;line-height:1.3}
  .interior-title{left:505px;top:440px;width:240px;color:var(--teal);font-size:19px;line-height:1.05}
  .uses{left:520px;top:490px;list-style:none;font-size:12px;line-height:1.35;color:#222}
  .uses li{display:flex;align-items:flex-start;gap:6px}
  .uses svg{width:12px;height:12px;margin-top:2px;flex:none}
</style>
</head>
<body>

<!-- FRONT -->
<section class="sheet sheet--front" aria-label="Vanjska strana letka">
  <svg class="art" viewBox="0 0 760 570" xmlns="http://www.w3.org/2000/svg">
    <defs>
      <linearGradient id="g-lawn" x1="0" y1="0" x2="0" y2="1"><stop offset="0" stop-color="#7f8a6c"/><stop offset=".55" stop-color="#8f9481"/><stop offset="1" stop-color="#4e8b34"/></linearGradient>
      <linearGradient id="g-flowers" x1="0" y1="0" x2="1" y2="1"><stop offset="0" stop-color="#3f7a2c"/><stop offset=".45" stop-color="#c9527f"/><stop offset="1" stop-color="#d98a6a"/></linearGradient>
      <linearGradient id="g-hedge" x1="0" y1="0" x2="1" y2="1"><stop offset="0" stop-color="#2f6b25"/><stop offset="1" stop-color="#4f9a33"/></linearGradient>
      <linearGradient id="g-wall" x1="0" y1="0" x2="0" y2="1"><stop offset="0" stop-color="#2f6a2a"/><stop offset=".5" stop-color="#6b7f8a"/><stop offset="1" stop-color="#b08c68"/></linearGradient>
      <radialGradient id="g-pool"><stop offset="0" stop-color="#3aa6d6"/><stop offset=".6" stop-color="#9fb6c2"/><stop offset="1" stop-color="#3f7d2f"/></radialGradient>
    </defs>
    <rect width="760" height="570" fill="#fff"/>
    <!-- left panel -->
    <rect x="0" y="0" width="245" height="570" fill="var(--green)"/>
    <path d="M0 150 L150 150 A95 95 0 0 0 245 55 L245 265 L0 265 Z" fill="#1d4b47"/>
    <rect x="0" y="0" width="205" height="150" fill="url(#g-lawn)" role="img" aria-label="Fotografija: ležaljka na umjetnom travnjaku uz živicu"/>
    <circle cx="192" cy="150" r="30" fill="var(--teal)" stroke="#fff" stroke-width="3"/>
    <path d="M192 134 l4.7 9.6 10.6 1.5 -7.7 7.5 1.8 10.5 -9.4-5 -9.4 5 1.8-10.5 -7.7-7.5 10.6-1.5z" fill="none" stroke="#fff" stroke-width="2" stroke-linejoin="round"/>
    <rect x="20" y="212" width="24" height="24" fill="#d8262f"/>
    <path d="M0 570 L0 330 Q110 250 245 228 L245 570 Z" fill="url(#g-flowers)" role="img" aria-label="Fotografija: umjetno cvijeće i stablo u izložbenom salonu"/>
    <path d="M0 322 Q110 242 245 220" fill="none" stroke="#fff" stroke-width="6"/>
    <!-- middle panel -->
    <rect x="245" y="0" width="255" height="570" fill="var(--panel-gray)"/>
    <rect x="245" y="0" width="255" height="200" fill="url(#g-hedge)" role="img" aria-label="Fotografija: zelena umjetna živica izbliza"/>
    <path d="M245 215 Q370 180 500 200 L500 235 Q370 212 245 245 Z" fill="var(--panel-gray)"/>
    <path d="M245 205 Q370 172 500 195" fill="none" stroke="#fff" stroke-width="5"/>
    <circle cx="300" cy="185" r="55" fill="#fff"/>
    <circle cx="300" cy="185" r="50" fill="var(--lime)"/>
    <path d="M245 505 Q380 468 500 478 L500 570 L245 570 Z" fill="var(--wood)"/>
    <path d="M245 500 Q380 462 500 472" fill="none" stroke="var(--teal)" stroke-width="4"/>
    <circle cx="380" cy="445" r="70" fill="var(--green)"/>
    <circle cx="380" cy="445" r="63" fill="url(#g-pool)" stroke="#fff" stroke-width="3" role="img" aria-label="Fotografija: bazen okružen umjetnom živicom"/>
    <!-- right panel -->
    <rect x="500" y="150" width="260" height="340" fill="url(#g-wall)" role="img" aria-label="Fotografija: vertikalni vrt s umjetnim zelenilom i pleteni stolci na terasi"/>
    <path d="M500 500 Q630 465 760 480 L760 570 L500 570 Z" fill="var(--wood)"/>
    <path d="M500 495 Q630 460 760 475" fill="none" stroke="var(--teal)" stroke-width="4"/>
    <circle cx="545" cy="478" r="44" fill="#fff"/>
    <circle cx="545" cy="478" r="40" fill="var(--teal)"/>
    <rect x="0" y="556" width="760" height="14" fill="var(--green)"/>
  </svg>

  <div class="abs wordmark wordmark--light" style="left:292px;top:20px"><span class="wordmark__dot"></span>KO-LNE d.o.o.</div>

  <div class="abs quality">
    <span class="quality__star">★</span>
    <span class="quality__word">QUALITY</span>
    <span class="quality__year">Since 1960</span>
    <span class="quality__stars">★★★</span>
  </div>

  <h2 class="abs salon-title script">Prodajno<br>izložbeni salon:</h2>
  <ul class="abs contact-list salon-contacts">
    <li><svg viewBox="0 0 10 10"><circle cx="5" cy="5" r="5" fill="var(--lime)"/><path d="M5 2.2a1.8 1.8 0 0 1 1.8 1.8C6.8 5.4 5 7.6 5 7.6S3.2 5.4 3.2 4A1.8 1.8 0 0 1 5 2.2z" fill="#fff"/></svg>LIPOVEC, Vrtna 8, 10431 Sv.Nedelja</li>
    <li><svg viewBox="0 0 10 10"><circle cx="5" cy="5" r="5" fill="var(--lime)"/><path d="M3.3 2.6l1 1-.5.8a3 3 0 0 0 1.8 1.8l.8-.5 1 1-.6.8C5 7.4 2.6 5 2.5 3.2z" fill="#fff"/></svg>+385 91 555 01 27</li>
    <li><svg viewBox="0 0 10 10"><circle cx="5" cy="5" r="5" fill="var(--lime)"/><path d="M3.3 2.6l1 1-.5.8a3 3 0 0 0 1.8 1.8l.8-.5 1 1-.6.8C5 7.4 2.6 5 2.5 3.2z" fill="#fff"/></svg>+385 98 555 046</li>
  </ul>
  <h3 class="abs seat-title script">Sjediste</h3>
  <ul class="abs contact-list seat-contacts">
    <li>KO-LNE d.o.o.</li>
    <li><svg viewBox="0 0 10 10"><circle cx="5" cy="5" r="5" fill="var(--lime)"/><path d="M5 2.2a1.8 1.8 0 0 1 1.8 1.8C6.8 5.4 5 7.6 5 7.6S3.2 5.4 3.2 4A1.8 1.8 0 0 1 5 2.2z" fill="#fff"/></svg>Ulica Javora 22, 10000 Zagreb</li>
    <li><svg viewBox="0 0 10 10"><circle cx="5" cy="5" r="5" fill="var(--lime)"/><rect x="2.5" y="3.3" width="5" height="3.4" fill="none" stroke="#fff" stroke-width=".8"/><path d="M2.5 3.3L5 5.2 7.5 3.3" fill="none" stroke="#fff" stroke-width=".8"/></svg>info@ko-lne.hr</li>
  </ul>
  <div class="abs web"><svg viewBox="0 0 12 12"><circle cx="6" cy="6" r="5.2" fill="none" stroke="var(--green-dark)" stroke-width="1.2"/><ellipse cx="6" cy="6" rx="2.2" ry="5.2" fill="none" stroke="var(--green-dark)" stroke-width="1"/><path d="M1 6h10" stroke="var(--green-dark)" stroke-width="1"/></svg>www.ko-lne.hr</div>

  <div class="abs wordmark wordmark--gray" style="left:520px;top:18px"><span class="wordmark__dot"></span>KO-LNE d.o.o.</div>
  <h1 class="abs tagline script">Prema Dimenzijama<br>i željama Kupaca</h1>
  <div class="abs badge-round inout-badge">Unutarnje<br>i vanjsko</div>
  <h2 class="abs service-title">UREĐENJE</h2>
  <p class="abs service-text">Poslovnih, stambenih, sportskih i ostalih objekata umjetnom živicom, dekorativnim zelenilom i cvijećem, drvećem i aranžmanima</p>
</section>

<!-- BACK -->
<section class="sheet sheet--back" aria-label="Unutarnja strana letka">
  <svg class="art" viewBox="0 0 760 570" xmlns="http://www.w3.org/2000/svg">
    <defs>
      <linearGradient id="g-pergola" x1="0" y1="0" x2="0" y2="1"><stop offset="0" stop-color="#c9d3da"/><stop offset=".35" stop-color="#c89a62"/><stop offset=".65" stop-color="#a8774a"/><stop offset="1" stop-color="#3d7a2c"/></linearGradient>
      <linearGradient id="g-trees" x1="0" y1="0" x2="0" y2="1"><stop offset="0" stop-color="#4f9a33"/><stop offset="1" stop-color="#2f6b25"/></linearGradient>
      <radialGradient id="g-deck"><stop offset="0" stop-color="#a35f3a"/><stop offset=".7" stop-color="#4b8a34"/><stop offset="1" stop-color="#8fb3c8"/></radialGradient>
      <linearGradient id="g-tub" x1="0" y1="0" x2="0" y2="1"><stop offset="0" stop-color="#3f7d2f"/><stop offset=".6" stop-color="#5d8a3a"/><stop offset="1" stop-color="#8b8f92"/></linearGradient>
    </defs>
    <rect width="760" height="570" fill="#fff"/>
    <ellipse cx="530" cy="55" rx="262" ry="162" fill="var(--lime-deep)"/>
    <ellipse cx="530" cy="50" rx="250" ry="150" fill="var(--lime)"/>
    <rect x="0" y="145" width="470" height="320" fill="url(#g-pergola)" role="img" aria-label="Fotografija: drvena pergola s ogradom od umjetne živice"/>
    <path d="M0 455 Q240 425 470 448 L470 570 L0 570 Z" fill="var(--green)"/>
    <rect x="10" y="455" width="170" height="108" fill="url(#g-trees)" role="img" aria-label="Fotografija: niz umjetnih ukrasnih stabala"/>
    <g fill="none" stroke="#fff" stroke-width="2" stroke-linejoin="round">
      <rect x="203" y="485" width="7" height="16"/>
      <path d="M210 487 h6 l3-9 a2.5 2.5 0 0 1 4 2 l-1 6 h7 a2 2 0 0 1 2 2.5 l-2 9 a2 2 0 0 1-2 1.5 h-17"/>
      <path d="M205 472 l-3-4 M211 470 v-5 M217 472 l3-4"/>
    </g>
    <circle cx="395" cy="450" r="66" fill="#fff"/>
    <circle cx="395" cy="450" r="62" fill="url(#g-deck)" role="img" aria-label="Fotografija: drvena terasa s pogledom na more i umjetnom živicom"/>
    <rect x="490" y="228" width="290" height="208" rx="14" fill="url(#g-tub)" role="img" aria-label="Fotografija: hidromasažna kada ispred zida od umjetne živice"/>
    <rect x="490" y="436" width="270" height="134" fill="var(--wood)"/>
    <rect x="748" y="0" width="12" height="570" fill="var(--green)"/>
    <circle cx="505" cy="185" r="41" fill="#fff"/>
    <circle cx="505" cy="185" r="37" fill="var(--teal)"/>
  </svg>

  <div class="abs wordmark wordmark--gray" style="left:20px;top:22px"><span class="wordmark__dot"></span>KO-LNE d.o.o.</div>
  <p class="abs history">KO-LNE d.o.o. osnovana je 1992 godine i nastavlja obiteljsku tradiciju započetu davne 1950 godine u obrtu Lavanda, a kasnije Lavanda-Zeleni kut sa pogonom u Sv.Nedelji kod Samobora.</p>
  <p class="abs offer">Bavimo se proizvodnjom umjetne živice, drveća, dekorativnog zelenila, umjetnog cvijeća i aranžmana za razne prigode (ukrasni buketi, cvjetni stupići, cvjetni kugli, grobnih aranžmana i sl.), kao, umjetnih latica u svim bojama i dezenima, bonsaia, žardinjera po narudžbi. Vanjsko i unutarnje uređenje poslovnih i trgovačkih centara, ugostiteljskih, stambenih i sportskih objekata, izrada scena za film i kazalište, wellness centri, bazeni, hoteli, ......</p>
  <div class="abs badge-round warranty">15-20<br>YEARS<br>COLOR<br>WARRANTY</div>
  <p class="abs clients">Naši brojni zadovoljni klijenti dokaz su vrhunske kvalitete naših proizvoda.</p>
  <h2 class="abs interior-title script">Unutarnje i vanjsko<br>uređenje prostora</h2>
  <ul class="abs uses">
    <li><svg viewBox="0 0 12 12"><path d="M2 10 C2 4 6 2 11 2 C11 7 8 10 2 10z" fill="var(--green)"/></svg>Umjetnom živicom</li>
    <li><svg viewBox="0 0 12 12"><path d="M2 10 C2 4 6 2 11 2 C11 7 8 10 2 10z" fill="var(--green)"/></svg>Drvećima</li>
    <li><svg viewBox="0 0 12 12"><path d="M2 10 C2 4 6 2 11 2 C11 7 8 10 2 10z" fill="var(--green)"/></svg>Dekorativnim zelenilom<br>i cvijećem</li>
  </ul>
</section>

</body>
</html>
```